Design website home page for pathology consulting company

Starting a new consulting company with anatomic pathologists focused on expert diagnosis and second opinions on difficult pathology cases. In the near future we will be incorporating next generation diagnostics for rare diseases of childhood into the business. These include discovery and testing of DNA for mutations.

The company is formed around one of the best known pathologists in the world named Harold "Juniper" Tolvik. The name of the company is "JuniperLab"

We had a logo design by ArtfulHive - it is great. I will attach file as soon as I have it (contest ending today). Our company is medical, uses microscopes, DNA, probably will focus on childhood diseases but not solely on childhood diseases. we're not particularly conservative, but the customers we want to appeal to include older practicing pathologists as well as patients (sometimes parents) looking for second opinions.

Think a group of expert doctors diagnosing disease through the microscope and through DNA technology, ages ranging from 35-75 all trained by the best pathologist in the world - "Juniper"

We receive glass slides from diseases from patients all over the world from docs who need an expert to tell them what is the diagnosis. So "path to the diagnosis" is also part of the company marketing message.

We want the website design to describe our company but be very simple to find what one is looking for as we will use it as the launch page to:
1) order services
2) check results/reports
3) set up new account
4) speak with one of the pathologists
5) see our test menu
6) access our educational material/webinars
Updates

Update - looking for home page design and then finalists will ask for second page design to keep with theme - ok?

Reason: realized this project isn't web design but web home page design - thanks

Reason: Holidays for some in next two weeks

Reason: Hot discussion among collaborators for a few of the submissions. Will provide detail individually this weekend. Thanks so much for all the submissions!

Target Market(s)

Referring pathologists, physicians who want second opinions on pathology disease diagnosis, patients who have had biopsies (either patients themselves or parents of patients), generally high education level

Industry/Entity Type

Marketing

Requirements
Must have
• JuniperLab
Next Generation Pathology Consultants

```html
<!DOCTYPE html>
<html lang="en">
<head>
<meta charset="utf-8">
<title>JuniperLab – Next Generation Pathology Consultants</title>
<link href="https://fonts.googleapis.com/css2?family=Arimo:ital,wght@0,400;0,700;1,400&display=swap" rel="stylesheet">
<style>
:root{
  --blue:#1f5597;
  --text:#555;
  --grey-nav:#ececec;
  --panel:#f1f1f1;
  --border:#999;
  --btn:#6e6e6e;
  --footer:#000;
  --footer-base:#343434;
}
*{margin:0;padding:0;box-sizing:border-box}
html,body{width:885px;height:1200px;overflow:hidden;background:#fff}
body{position:relative;font-family:"Arimo",Arial,sans-serif;color:var(--text)}
.abs{position:absolute}
.brand-name{left:62px;top:90px;font-size:25px;color:var(--blue);line-height:1;font-weight:400}
.account{right:63px;top:22px;font-size:19px;color:var(--blue);display:flex}
.account span{padding:0 6px}
.account span+span{border-left:1px solid var(--blue)}
.call{right:143px;top:86px;text-align:right;color:var(--blue);line-height:1;border-right:1px solid var(--blue);padding-right:8px}
.call .lbl{font-size:15px}
.call .num{font-size:19px;margin-top:2px}
.social{display:flex;gap:5px}
.social i{display:block;width:19px;height:19px}
.s1{background:#5cb6df}.s2{background:#f08c1e}.s3{background:#3b5a9a}
.nav{left:19px;top:134px;width:847px;height:60px;background:var(--grey-nav);display:flex;align-items:center}
.nav a{color:#777;text-decoration:none;font-size:13.5px;text-align:center;line-height:1.25;flex:1}
.nav a.active{flex:0 0 106px;height:60px;background:var(--blue);color:#fff;display:flex;align-items:center;justify-content:center}
.hero{left:19px;top:200px;width:847px;height:255px;border:2px solid var(--blue);background:linear-gradient(90deg,#3f74b3 0%,#7ea7d2 40%,#c9dced 65%,#e9eef3 100%)}
.hero-btn{left:54px;top:147px;width:157px;height:37px;background:#eee;border:1px solid #ccc;color:#666;font-weight:700;font-size:15px;display:flex;align-items:center;justify-content:center;letter-spacing:.5px}
.arrow{top:103px;width:24px;height:42px;background:rgba(230,236,244,.85);display:flex;align-items:center;justify-content:center}
.dots{left:395px;top:243px;display:flex;gap:3px}
.dots i{width:7px;height:7px;border-radius:50%;background:#fff}
.dots i:first-child{background:#3d6ea9}
h2{position:absolute;font-weight:400;color:var(--blue);font-size:19px}
.why{left:19px;top:503px;width:265px;height:312px;border:1px solid var(--border);background:var(--panel)}
.why ul{list-style:none;position:absolute;left:10px;top:15px}
.why li{font-size:12px;color:var(--blue);height:29.5px}
.why li::before{content:"›";color:#777;margin-right:5px}
.small{font-size:9.6px;line-height:11.7px;color:#555}
.why .small{position:absolute;left:9px;top:145px;width:246px}
.btn{left:138px;top:266px;width:115px;height:36px;background:var(--btn);color:#fff;border-radius:3px;font-size:15px;display:flex;align-items:center;justify-content:center}
.testi{left:19px;top:850px;width:265px;height:203px;border:1px solid #bbb}
.testi .small{position:absolute;left:37px;top:11px;width:222px;font-size:9.1px}
.quote{font-family:Georgia,serif;font-size:44px;color:#ddd;line-height:1}
.testi .name{position:absolute;left:13px;top:162px;font-size:15px;color:var(--blue)}
.testi .date{position:absolute;left:13px;top:180px;font-size:9px;font-style:italic;color:#555}
.body{font-size:11.2px;line-height:14px;color:#555}
.photo{background:linear-gradient(135deg,#cfd6de,#eef0f2 50%,#b8c0c8);border:1px solid var(--blue)}
.footer{left:0;top:1064px;width:885px;height:56px;background:var(--footer);display:flex;justify-content:center;align-items:center}
.footer a{color:#ccc;text-decoration:none;font-size:9.6px;text-align:center;line-height:12px;padding:0 5px;border-left:1px solid #555}
.footer a:first-child{border-left:0}
.base{left:0;top:1120px;width:885px;height:80px;background:var(--footer-base)}
.copy{left:110px;top:10px;font-size:9.6px;color:#ccc}
</style>
</head>
<body>
<header>
  <div class="abs brand-name">JuniperLab</div>
  <div class="abs account"><span>Register</span><span>Login</span></div>
  <div class="abs call"><div class="lbl">Call Us</div><div class="num">000 000 0000</div></div>
  <div class="abs social" style="left:754px;top:94px"><i class="s1"></i><i class="s2"></i><i class="s3"></i></div>
  <nav class="abs nav">
    <a class="active">Home</a><a>About Us</a><a>Order services</a><a>Check<br>Results / Reports</a><a>Speak with<br>pathologists</a><a>Test menu</a><a>Educational<br>material</a><a>Contact Us</a>
  </nav>
</header>

<section class="abs hero" role="img" aria-label="Scientist in safety glasses and blue gloves using a pipette beside laboratory glassware">
  <div class="abs arrow" style="left:6px"><svg width="10" height="22"><path d="M8 1L2 11l6 10" stroke="#3d6ea9" stroke-width="3" fill="none"/></svg></div>
  <div class="abs arrow" style="right:6px"><svg width="10" height="22"><path d="M2 1l6 10-6 10" stroke="#3d6ea9" stroke-width="3" fill="none"/></svg></div>
  <div class="abs hero-btn">REGISTER NOW</div>
  <div class="abs dots"><i></i><i></i><i></i><i></i></div>
</section>

<h2 style="left:19px;top:465px">Why Choose Us</h2>
<aside class="abs why">
  <ul>
    <li>Expert diagnosis</li>
    <li>Incorporating next generation diagnostics</li>
    <li>Discovery &amp; testing of DNA for mutations</li>
    <li>Why Choose Us</li>
  </ul>
  <div class="small">Lorem ipsum dolor sit amet, consectetur adipisicing elit, sed do or incididunt ut labore et dolore magna aliqua. Ut enim ad minim am, quis trud exercitation ullamco laboris nisi ut aliquip ex ea comodo consequa.Lorem olor sit amet, consectetur adipisicing elit, sed do eiusmod tempor incididunt ut abore et dolore magna aliqua. Ut im ad minim veniam, quis.<br><br>Lorem ipsum dolor sit amet, consectetur adipisicing elit.</div>
  <div class="abs btn">Read more..</div>
</aside>

<h2 style="left:22px;top:822px">Testimonials</h2>
<svg class="abs" style="left:240px;top:826px" width="32" height="16"><path d="M7 2L3 8l4 6M25 2l4 6-4 6" stroke="#555" stroke-width="2.5" fill="none"/></svg>
<section class="abs testi">
  <div class="abs quote" style="left:10px;top:4px">“</div>
  <div class="small">Lorem ipsum dolor sit amet, consectetur adipisicing elit, sed do or incididunt ut labore et dolore magna aliqua. Ut enim ad minim am, quis trud exercitation ullamco laboris nisi ut aliquip ex ea comodo consequa.Lorem olor sit amet, consectetur adipisicing elit, sed do eiusmod tempor incididunt ut abore et dolore magna aliqua. Ut im ad minim veniam, quis.<br><br>Lorem ipsum dolor sit amet, consectetur adipisicing elit, sed do or incididunt ut labore et dolore magna aliqua.</div>
  <div class="abs quote" style="left:232px;top:132px">”</div>
  <div class="name">Name</div>
  <div class="date">Posted on 20 June 2013</div>
</section>

<h2 style="left:301px;top:465px">Welcome to JuniperLab</h2>
<div class="abs body" style="left:300px;top:503px;width:340px">Lorem ipsum dolor sit amet, consectetur adipisicing elit, sed do or incididunt ut labore et dolore magna aliqua. Ut enim ad minim am, quis trud exercitation ullamco laboris nisi ut aliquip ex ea comodo consequa.Lorem olor sit amet, consectetur adipisicing elit, sed do eiusmod tempor incididunt ut abore et dolore magna aliqua. Ut im ad minim veniam, quis.<br><br><br>Lorem ipsum dolor sit amet, consectetur adipisicing elit, sed do or incididunt ut labore et dolore magna aliqua. Ut enim ad minim am, quis trud exercitation ullamco laboris nisi ut aliquip ex ea comodo consequa.Lorem olor sit amet, consectetur adipisicing elit, sed do eiusmod tempor incididunt ut abore et dolore magna aliqua. Ut im ad minim veniam, quis.<br><br>Lorem ipsum dolor sit amet, consectetur adipisicing elit, sed do or incididunt.</div>
<div class="abs photo" style="left:648px;top:503px;width:218px;height:240px" role="img" aria-label="Senior doctor with a stethoscope looking into a microscope"></div>
<div class="abs body" style="left:300px;top:748px;width:568px">Lorem ipsum dolor sit amet, consectetur adipisicing elit, sed do or incididunt ut labore et dolore magna aliqua. Ut enim ad minim am, quis trud exercitation ullamco laboris nisi ut aliquip ex ea comodo consequa.Lorem olor sit amet, consectetur adipisicing elit, sed do eiusmod tempor incididunt ut abore et dolore magna aliqua. Ut im ad minim veniam, quis.<br><br>Lorem ipsum dolor sit amet, consectetur adipisicing elit, sed do or incididunt ut labore et dolore magna aliqua. Ut enim ad minim am, quis trud exercitation ullamco laboris nisi ut aliquip ex ea comodo consequa.Lorem olor sit amet, consectetur adipisicing agna aliqua. Ut im ad minim veniam, quis.</div>

<h2 style="left:305px;top:873px">Our Services “Path to correct Diagnosis”</h2>
<div class="abs photo" style="left:300px;top:917px;width:122px;height:145px;background:linear-gradient(160deg,#b9c8d8,#e6ebef 55%,#aebdcc)" role="img" aria-label="Glass slide with a blood sample"></div>
<div class="abs body" style="left:428px;top:920px;width:440px">Lorem ipsum dolor sit amet, consectetur adipisicing elit, sed do or incididunt ut labore et dolore magna aliqua. Ut enim ad minim am, quis trud exercitation ullamco laboris nisi ut aliquip ex ea comodo consequa.Lorem olor sit amet, consectetur adipisicing agna aliqua. Ut im ad minim veniam, quis.<br><br>Lorem ipsum dolor sit amet, consectetur adipisicing elit, sed do or incididunt ut labore et dolore magna aliqua. Ut enim ad minim am, quis trud exercitation ullamco laboris nisi ut aliquip ex ea comodo consequa.Lorem olor sit amet, consectetur adipisicing agna aliqua. Ut im ad minim veniam, quis.</div>

<footer>
  <nav class="abs footer">
    <a>Home</a><a>About Us</a><a>Order services</a><a>Check<br>Results / Reports</a><a>Speak with<br>pathologists</a><a>Test menu</a><a>Educational<br>material</a><a>Contact Us</a>
  </nav>
  <div class="abs base">
    <div class="abs copy">Copyright © 2013 JuniperLab. All Right reaerved.</div>
    <div class="abs social" style="left:586px;top:6px;gap:6px"><i class="s1" style="width:24px;height:26px"></i><i class="s2" style="width:24px;height:26px"></i><i class="s3" style="width:24px;height:26px"></i></div>
  </div>
</footer>
</body>
</html>
```